Business Cards, Letterhead and Email signature for Halvern Building Collective
Halvern Building Collective
Professional
Doran Pellick
Partner
Office: 4100 Birchmont Ave Suite 900 Charlotte, NC 28211
Mailing: 5217 Birchmont Ave #482 Charlotte, NC 28211
dpellick@halvernbuildingcoll.example
halvvernbuildingcoll.example
I am open to ideas, maybe the logo with a matching background color. Be creative

```html
<!DOCTYPE html>
<html lang="en">
<head>
<meta charset="utf-8">
<title>Halvern Building Collective — Business Card</title>
<link rel="stylesheet" href="https://fonts.googleapis.com/css2?family=Michroma&display=swap">
<style>
  :root {
    --backdrop: #e9e7e3;
    --card-white: #ffffff;
    --brand-blue: #1f4ea3;
    --band-blue-top: #2c5cb8;
    --band-blue-bottom: #183f8a;
    --tab-grey: #4a4c50;
    --tab-grey-dark: #38393c;
    --name-grey: #d9dadc;
    --title-grey: #b5b7ba;
    --contact-white: #ffffff;
  }
  * { box-sizing: border-box; margin: 0; padding: 0; }
  html, body {
    width: 1200px; height: 900px; overflow: hidden;
    background: var(--backdrop);
    font-family: "Michroma", sans-serif;
  }
  .canvas { position: relative; width: 1200px; height: 900px; }
  .card {
    position: absolute; left: 100px; top: 164px;
    width: 1000px; height: 572px;
    background: var(--card-white);
    overflow: hidden;
    box-shadow: 0 6px 24px rgba(0,0,0,0.18);
  }
  .card__band {
    position: absolute; left: 0; right: 0; top: 240px; bottom: 0;
    background: linear-gradient(180deg, var(--band-blue-top) 0%, var(--band-blue-bottom) 100%);
  }
  .brand {
    position: absolute; left: 48px; top: 92px;
    display: flex; align-items: center; gap: 22px;
  }
  .brand__mark {
    width: 96px; height: 96px; background: var(--brand-blue);
  }
  .brand__name {
    color: var(--brand-blue);
    font-size: 27px; letter-spacing: 0.5px;
    text-transform: uppercase; line-height: 1;
  }
  .name-tab {
    position: absolute; right: 0; top: 212px;
    width: 420px; height: 92px;
    background: linear-gradient(180deg, var(--tab-grey) 0%, var(--tab-grey-dark) 100%);
    clip-path: polygon(0 0, 100% 0, 100% 100%, 28px 100%, 0 72px);
    text-align: center; padding-top: 22px;
  }
  .name-tab__name {
    color: var(--name-grey); font-size: 19px; letter-spacing: 2px;
    font-variant: small-caps;
  }
  .name-tab__title {
    margin-top: 8px; color: var(--title-grey); font-size: 11px;
    letter-spacing: 2px; text-transform: uppercase;
  }
  .contact {
    position: absolute; left: 48px; top: 378px;
    list-style: none; color: var(--contact-white);
    font-size: 13px; letter-spacing: 0.6px; line-height: 1.55;
  }
  .contact__item { display: flex; align-items: flex-start; gap: 10px; }
  .contact__icon {
    flex: none; width: 15px; height: 15px; margin-top: 2px;
  }
  .contact__text { text-transform: uppercase; }
  .website {
    position: absolute; right: 48px; top: 418px;
    color: var(--contact-white); font-size: 13px; letter-spacing: 0.8px;
    text-transform: uppercase;
  }
</style>
</head>
<body>
<main class="canvas">
  <section class="card" aria-label="Business card for Halvern Building Collective">
    <div class="card__band"></div>

    <div class="brand">
      <span class="brand__mark" aria-hidden="true"></span>
      <span class="brand__name">Halvern Building Collective</span>
    </div>

    <div class="name-tab">
      <p class="name-tab__name">Doran Pellick</p>
      <p class="name-tab__title">Partner</p>
    </div>

    <ul class="contact">
      <li class="contact__item">
        <svg class="contact__icon" viewBox="0 0 16 16" aria-hidden="true">
          <circle cx="8" cy="8" r="8" fill="#fff"/>
          <path d="M8 3.5a3 3 0 0 0-3 3c0 2.2 3 5.8 3 5.8s3-3.6 3-5.8a3 3 0 0 0-3-3zm0 4.1a1.1 1.1 0 1 1 0-2.2 1.1 1.1 0 0 1 0 2.2z" fill="#1f4ea3"/>
        </svg>
        <span class="contact__text">4100 Birchmont Ave Suite<br>900 Charlotte, NC 28211</span>
      </li>
      <li class="contact__item">
        <svg class="contact__icon" viewBox="0 0 16 16" aria-hidden="true">
          <circle cx="8" cy="8" r="8" fill="#fff"/>
          <path d="M5.2 4h1.6l.8 2-1 .8a5 5 0 0 0 2.6 2.6l.8-1 2 .8v1.6c0 .5-.4.9-.9.9A7 7 0 0 1 4.3 4.9c0-.5.4-.9.9-.9z" fill="#1f4ea3"/>
        </svg>
        <span class="contact__text">704-555-0182</span>
      </li>
      <li class="contact__item">
        <svg class="contact__icon" viewBox="0 0 16 16" aria-hidden="true">
          <circle cx="8" cy="8" r="8" fill="#fff"/>
          <rect x="5.5" y="3.5" width="5" height="9" rx="1" fill="#1f4ea3"/>
          <rect x="6.5" y="4.7" width="3" height="5.5" fill="#fff"/>
        </svg>
        <span class="contact__text">704-555-0147</span>
      </li>
      <li class="contact__item">
        <svg class="contact__icon" viewBox="0 0 16 16" aria-hidden="true">
          <circle cx="8" cy="8" r="8" fill="#fff"/>
          <rect x="4" y="7" width="8" height="5" fill="#1f4ea3"/>
          <rect x="5.5" y="3.8" width="5" height="3.6" fill="#1f4ea3"/>
        </svg>
        <span class="contact__text">704-555-0193</span>
      </li>
      <li class="contact__item">
        <svg class="contact__icon" viewBox="0 0 16 16" aria-hidden="true">
          <circle cx="8" cy="8" r="8" fill="#fff"/>
          <rect x="3.8" y="5" width="8.4" height="6" fill="#1f4ea3"/>
          <path d="M3.8 5 8 8.3 12.2 5" fill="none" stroke="#fff" stroke-width="0.9"/>
        </svg>
        <span class="contact__text">dpellick@halvernbuildingcoll.example</span>
      </li>
      <li class="contact__item">
        <svg class="contact__icon" viewBox="0 0 16 16" aria-hidden="true">
          <circle cx="8" cy="8" r="8" fill="#fff"/>
          <circle cx="8" cy="8" r="4.3" fill="none" stroke="#1f4ea3" stroke-width="1"/>
          <ellipse cx="8" cy="8" rx="1.8" ry="4.3" fill="none" stroke="#1f4ea3" stroke-width="0.9"/>
          <path d="M3.7 8h8.6" stroke="#1f4ea3" stroke-width="0.9"/>
        </svg>
        <span class="contact__text">www.halvernbuildingcoll.example</span>
      </li>
    </ul>

    <p class="website">www.halvernbuildingcoll.example</p>
  </section>
</main>
</body>
</html>
```